Tidewater Ridge Podiatry

Please design a flyer using the same layout/font/colours ect as the business card (attached) please make the flyer with curved corners.
Front of DL flyer: (vertical)
Business name & logo (same as card attached)
Treatments include:
-foot, ankle & leg pain
-heel pain
-nail care
-corn & callus treatment
-bunion advice
-mechanical assessments
-orthotics
-nail surgery

Consulting within 'Bellwind Family Pharmacy' ApolloBay.
47-49 Tillbrook Parade, Corrin Bay.
Call for appointments: 0411 837 260

Email:tidewaterridgepodiatry@pelmornmail.net

Reverse of flyer (horizontal)
Business name & logo

Derek Hollins
B.Pod.
B.App.Sci (HM)
NWMBQ Reg: Pod 0007384251

0422 716 308

RHS,KMB & LWF registered provider
Private Health Insurance-ancillaries cover.

```html
<!DOCTYPE html>
<html lang="en">
<head>
<meta charset="utf-8">
<title>Tidewater Ridge Podiatry – DL Flyer</title>
<link rel="stylesheet" href="https://fonts.googleapis.com/css2?family=Exo+2:wght@500;600;700&family=Lato:wght@400;700&display=swap">
<style>
  :root {
    --teal: #47b8c9;
    --teal-deep: #3aaabb;
    --charcoal: #555557;
    --ink: #1f1f21;
    --paper: #ffffff;
    --backdrop: #ece9e4;
    --label: #6b655d;
  }
  * { margin: 0; padding: 0; box-sizing: border-box; }
  html, body { width: 1105px; height: 1200px; overflow: hidden; }
  body { background: var(--backdrop); position: relative; font-family: "Lato", sans-serif; }

  .flyer {
    position: absolute; top: 80px; width: 478px; height: 977px;
    background: var(--paper); overflow: hidden;
    box-shadow: 0 6px 18px rgba(0,0,0,.18);
  }
  .flyer--front { left: 63px; }
  .flyer--back { left: 577px; }
  .flyer__shapes { position: absolute; inset: 0; width: 100%; height: 100%; }

  .line {
    position: absolute; left: 0; right: 0; text-align: center; white-space: nowrap;
  }
  .display { font-family: "Exo 2", sans-serif; font-weight: 600; letter-spacing: 1px; }

  .brand-mark {
    position: absolute; left: 50%; width: 64px; height: 64px; margin-left: -32px;
    border-radius: 50%;
  }
  .brand-name { font-family: "Exo 2", sans-serif; font-weight: 500; }
  .brand-name--top { font-size: 32px; letter-spacing: .5px; }
  .brand-name--sub { font-size: 21px; letter-spacing: 7px; }

  .on-teal { color: var(--paper); }
  .on-dark { color: var(--ink); }

  /* front */
  .treatments__title { color: var(--teal); font-size: 27px; letter-spacing: 2px; }
  .treatments__item { font-weight: 700; font-size: 16px; color: var(--ink); }
  .treatments__item::before { content: "\27A4"; color: var(--teal); font-size: 10px; margin-right: 3px; vertical-align: 2px; }
  .consult__title { font-size: 30px; }
  .consult__venue { font-size: 14.5px; letter-spacing: 1px; }
  .consult__address { font-family: "Lato", sans-serif; font-size: 17px; font-weight: 400; }
  .consult__call { font-size: 17px; }
  .contact { font-family: "Lato", sans-serif; font-weight: 700; font-size: 17px; }
  .contact svg { vertical-align: -2px; margin-right: 6px; }

  /* back */
  .practitioner__name { font-size: 31px; font-weight: 700; letter-spacing: 2px; }
  .practitioner__cred { font-size: 21px; font-weight: 500; letter-spacing: 1px; }
  .practitioner__phone { font-size: 40px; font-weight: 600; letter-spacing: 3px; }
  .practitioner__phone svg { vertical-align: -3px; margin-right: 4px; }
  .provider { font-size: 23px; font-weight: 600; letter-spacing: 1.5px; }
  .insurance { font-size: 23px; font-weight: 600; letter-spacing: .5px; }

  .side-label {
    position: absolute; top: 1098px; width: 478px; text-align: center;
    font-family: "Lato", sans-serif; font-weight: 700; font-size: 31px; color: var(--label);
  }
</style>
</head>
<body>

<!-- Front of flyer -->
<section class="flyer flyer--front">
  <svg class="flyer__shapes" viewBox="0 0 429 877" preserveAspectRatio="none" aria-hidden="true">
    <path fill="var(--teal)" d="M0 0H429V108C330 185 190 258 0 262Z"/>
    <path fill="var(--charcoal)" d="M0 138C55 200 150 242 250 252C150 256 60 250 0 246Z"/>
    <path fill="var(--teal)" d="M0 768C55 660 190 578 300 578C360 578 400 588 429 598V877H0Z"/>
    <path fill="var(--charcoal)" d="M180 614C290 596 395 625 429 675V790C395 705 300 635 180 614Z"/>
  </svg>

  <span class="brand-mark" style="top:62px;background:var(--paper);opacity:.9"></span>
  <p class="line brand-name brand-name--top on-teal" style="top:148px">Tidewater Ridge</p>
  <p class="line brand-name brand-name--sub on-teal" style="top:186px">Podiatry</p>

  <h2 class="line display treatments__title" style="top:342px">TREATMENTS INCLUDE:</h2>
  <ul class="treatments" style="list-style:none">
    <li class="line treatments__item" style="top:392px">Foot, ankle &amp; leg pain</li>
    <li class="line treatments__item" style="top:421px">Heel pain</li>
    <li class="line treatments__item" style="top:450px">Nail care</li>
    <li class="line treatments__item" style="top:479px">Corn &amp; callus treatment</li>
    <li class="line treatments__item" style="top:508px">Bunion advice</li>
    <li class="line treatments__item" style="top:537px">Mechanical assessments</li>
    <li class="line treatments__item" style="top:566px">Orthotics</li>
    <li class="line treatments__item" style="top:595px">Nail surgery</li>
  </ul>

  <h3 class="line display consult__title on-teal" style="top:758px">Consulting within</h3>
  <p class="line display consult__venue on-teal" style="top:802px">'Bellwind Family Pharmacy' CorrinBay</p>
  <p class="line consult__address on-teal" style="top:828px">47-49 Tillbrook Parade, Corrin Bay</p>
  <p class="line display consult__call on-teal" style="top:860px">Call for appointments:</p>
  <p class="line contact on-dark" style="top:889px">
    <svg width="13" height="15" viewBox="0 0 24 24"><path fill="#444" d="M6.6 10.8a15.1 15.1 0 006.6 6.6l2.2-2.2c.3-.3.7-.4 1-.2 1.1.4 2.3.6 3.6.6.6 0 1 .4 1 1V20c0 .6-.4 1-1 1A17 17 0 013 4c0-.6.4-1 1-1h3.5c.6 0 1 .4 1 1 0 1.3.2 2.5.6 3.6.1.3 0 .7-.2 1z"/></svg>0411 837 260</p>
  <p class="line contact on-dark" style="top:914px;font-size:15.5px">
    <svg width="14" height="11" viewBox="0 0 24 18"><rect width="24" height="18" fill="#444"/><path d="M1 1l11 9 11-9" fill="none" stroke="#fff" stroke-width="2"/></svg>tidewaterridgepodiatry@pelmornmail.net</p>
</section>

<!-- Reverse of flyer -->
<section class="flyer flyer--back">
  <svg class="flyer__shapes" viewBox="0 0 429 877" preserveAspectRatio="none" aria-hidden="true">
    <path fill="var(--teal)" d="M0 0H429V210C380 310 280 372 150 372C90 372 40 360 0 345Z"/>
    <path fill="var(--charcoal)" d="M0 250C40 310 130 350 250 360C150 372 60 350 0 330Z"/>
    <path fill="var(--teal)" d="M0 778C50 670 180 590 300 590C360 590 400 600 429 610V877H0Z"/>
    <path fill="var(--charcoal)" d="M180 626C290 606 395 638 429 688V790C395 715 300 648 180 626Z"/>
  </svg>

  <h1 class="line display practitioner__name on-teal" style="top:28px">DEREK HOLLINS</h1>
  <p class="line display practitioner__cred on-dark" style="top:80px">B.Pod.</p>
  <p class="line display practitioner__cred on-dark" style="top:117px">B.App.Sci (HM)</p>
  <p class="line display practitioner__cred on-dark" style="top:157px">NWMBQ Reg: Pod 0007384251</p>
  <p class="line display practitioner__phone on-teal" style="top:236px">
    <svg width="28" height="32" viewBox="0 0 24 24"><path fill="#4a4a4c" d="M6.6 10.8a15.1 15.1 0 006.6 6.6l2.2-2.2c.3-.3.7-.4 1-.2 1.1.4 2.3.6 3.6.6.6 0 1 .4 1 1V20c0 .6-.4 1-1 1A17 17 0 013 4c0-.6.4-1 1-1h3.5c.6 0 1 .4 1 1 0 1.3.2 2.5.6 3.6.1.3 0 .7-.2 1z"/></svg>0422 716 308</p>

  <span class="brand-mark" style="top:498px;background:var(--teal)"></span>
  <p class="line brand-name brand-name--top" style="top:574px;color:var(--teal)">Tidewater Ridge</p>
  <p class="line brand-name brand-name--sub" style="top:611px;color:var(--teal)">Podiatry</p>

  <p class="line display provider on-teal" style="top:780px">RHS,KMB &amp; LWF</p>
  <p class="line display provider on-teal" style="top:809px">REGISTERED PROVIDER</p>
  <p class="line display insurance on-dark" style="top:867px">Private Health</p>
  <p class="line display insurance on-dark" style="top:896px">Insurance-ancillaries cover</p>
</section>

<p class="side-label" style="left:63px">FRONT</p>
<p class="side-label" style="left:577px">BACK</p>

</body>
</html>
```